Classic Personal Business Card in Regatta Dane Whitcomb Style (Horizontal - Raised Ink)

If you ever seen a Dane Whitcomb Regatta shirt, you will know that the signature of that shirt is small monogrammed icon on the left pocket. I envision my personal business card using some of these elements. I am in the oil exploration industry, which is very conservative and I want a card that looks great but still reflects that classic conservatism. I specifically do land management work, which means I determine who owns mineral rights, I lease those rights for larger companies to then drill for crude oil and natural gas

1. I have designed a small logo (which definitely could use some help) that I would like to be pretty small, centered in the middle of the card, and near the top of the card (color - navy blue or similar) Please feel free to make this logo infinitely better. However, I am not looking for anything abstract/

2. I want my name and designation (Morgan D. Hartwell, RPL) centered in the middle of the card. As far as font, I'm looking for a classic, strong (almost masculine) cursive font (I realize masculine + cursive is a little oxymoronic) and I would like it to the color to be Gold.

3. I would like my name (see above) to sit on top of a thin, centered navy blue (or similar) line as if it were almost a signature on a line. I want the lower-case letters that normally would dip below the line (which is y and p in my case) to do the same. I'll attach an example to help illustrate what I mean.

4. The rest of the card is my contact information. Because I am shoot for a more centered and balance look, I would like the placement of my contact information to also be centered and balance. Font should be a very classic, professional font. My first inclination is to use black for the color but I'm open to other suggestions.

Contact information:

Phone: (555) 014-2387
Email: mdhartwl@qovantri.com

Important Note: My hope is to have these printed with Raised Ink on High Quality High Quality Card Stock so it must conform to this Necessity.

Project Deadline Extended Reason: I am having major internet trouble. So I am not able to look at the submissions and provide feedback in a timely fashion. Also, it is difficult to access the site from just my phone. Added Saturday, November 22, 2014

Target Market(s)

US Oil Executives

Industry/Entity Type

Conservative

Contact Information for Business Card

I've posted a new logo that needs some clean up and a new idea for the top and bottom border of the card. I would like the logo to be centered in the top border with a white barrier on either side between the logo and the border. I've also posted color codes below.

Thanks

Requirements
Must have
• Color Codes:
• Blue: R - 0 G - 0 B - 102
• Gold R - 102 G - 102 B - 0

```html
<!DOCTYPE html>
<html lang="en">
<head>
<meta charset="utf-8">
<title>Morgan D. Hartwell, RPL – Business Card</title>
<link rel="stylesheet" href="https://fonts.googleapis.com/css2?family=Open+Sans:wght@400&display=swap">
<style>
  :root {
    --backdrop: #ecebe8;
    --card: #ffffff;
    --ink: #1f1f1f;
    --rule: #4b3f92;
    --emblem-fill: #1c8fd6;
    --emblem-edge: #1b1560;
    --shadow: rgba(0, 0, 0, 0.18);
  }
  * { margin: 0; padding: 0; box-sizing: border-box; }
  html, body {
    width: 1200px;
    height: 1000px;
    overflow: hidden;
    background: var(--backdrop);
  }
  .canvas {
    position: relative;
    width: 1200px;
    height: 1000px;
  }
  .business-card {
    position: absolute;
    left: 150px;
    top: 243px;
    width: 900px;
    height: 514px;
    background: var(--card);
    box-shadow: 0 10px 30px var(--shadow);
    font-family: "Open Sans", "Segoe UI", sans-serif;
    color: var(--ink);
    text-align: center;
  }
  .emblem {
    position: absolute;
    left: 50%;
    top: 52px;
    width: 116px;
    height: 116px;
    margin-left: -58px;
  }
  .holder-name {
    position: absolute;
    left: 0;
    right: 0;
    top: 196px;
    font-size: 46px;
    line-height: 1.2;
    font-weight: 400;
    letter-spacing: 0.2px;
  }
  .holder-name .signature {
    text-decoration: underline;
    text-decoration-color: var(--rule);
    text-decoration-thickness: 2px;
    text-underline-offset: 6px;
    text-decoration-skip-ink: none;
  }
  .contact-list {
    position: absolute;
    left: 0;
    right: 0;
    top: 282px;
    list-style: none;
    font-size: 33px;
    line-height: 1.3;
  }
</style>
</head>
<body>
  <main class="canvas">
    <section class="business-card" aria-label="Business card of Morgan D. Hartwell, RPL">
      <svg class="emblem" viewBox="0 0 116 116" aria-hidden="true">
        <circle cx="58" cy="58" r="56" fill="var(--emblem-fill)" stroke="var(--emblem-edge)" stroke-width="2"/>
      </svg>
      <h1 class="holder-name"><span class="signature">Morgan D. Hartwell</span>, RPL</h1>
      <ul class="contact-list">
        <li class="contact-phone">Phone: (555) 014-2387</li>
        <li class="contact-email">Email: mdhartwl@qovantri.com</li>
      </ul>
    </section>
  </main>
</body>
</html>
```